Admin Backend Redesign

We need a redesign for our backend which supoosed to make the backoffice look more modern!

I will add screenshots of the backoffice so you know what data will be shown in the Admin.

Have in mind that the users of this backend are Doctors. We need a clinical look, modern and sharp. The backoffice is responsive, have that in mind. We need the backoffice to look as professional as possible.

The theme used for the website is: http://velmora.quillstack-sample.com/

ON the main page of the backoffice, under every widget i need some space to write an explanation what the widget is about.

The color code used in our logo and website is #57aad4 combined with white.

We are open for ideas!
Updates

Project Deadline Extended
Reason: Designs are ok, but nothing innovative. Please use more modern designs!

Project Deadline Extended
Reason: Havent recieved a perfect design yet. Please read instructions carefully! Thank you

Project Deadline Extended
Reason: Hey everybody, sorry for the delay. We will decide in 3 days. If anyone wants to add a Design, that would be great.

Target Market(s)

Doctors, therapists

Industry/Entity Type

It Professional

Font styles to use
Sans Serif

Requirements
Must have
• Must look uptodate, modern, like new back offices look nowadays

```html
<!DOCTYPE html>
<html lang="de">
<head>
<meta charset="utf-8">
<title>Dashboard</title>
<link href="https://fonts.googleapis.com/css2?family=Roboto:wght@300;400;500&display=swap" rel="stylesheet">
<style>
:root{
  --blue:#1a9cda;
  --blue-dark:#0f86c3;
  --ink:#444;
  --muted:#6d7a84;
  --line:#e2e2e2;
  --panel:#f4f4f4;
  --grey-btn:#8c8c8c;
  --icon-btn:#8e8e8e;
  --footer:#5a5a5a;
  --s1:#4394c0;
  --s2:#64717c;
  --s3:#2a3540;
}
*{box-sizing:border-box;margin:0;padding:0}
html,body{width:1200px;height:1104px;overflow:hidden}
body{font-family:'Roboto',sans-serif;color:var(--ink);position:relative;
  background:repeating-linear-gradient(135deg,#f8f8f8 0 2px,#f1f1f1 2px 3px);}
.topline{position:absolute;top:0;left:0;width:1200px;height:2px;background:var(--blue)}
.stripe{position:absolute;top:63px;left:0;width:1200px;height:53px;
  background:repeating-linear-gradient(135deg,#e6e6e6 0 2px,#d9d9d9 2px 4px)}
.wrap{position:absolute;left:161px;width:878px}
.logo{top:14px;font-size:29px;font-weight:400;color:#6a6a6a;letter-spacing:.5px}
.userbar{position:absolute;top:15px;right:161px;display:flex;gap:10px}
.ibtn{width:30px;height:28px;border-radius:3px;background:var(--icon-btn);display:flex;align-items:center;justify-content:center}
.user{height:28px;border-radius:3px;background:var(--icon-btn);color:#fff;font-size:13.5px;display:flex;align-items:center;padding-left:12px}
.user .caret{margin-left:12px;width:26px;height:100%;border-left:1px solid #a9a9a9;display:flex;align-items:center;justify-content:center}
.nav{top:57px;height:64px;background:linear-gradient(#1aa0de,var(--blue-dark));display:flex;padding-left:17px;gap:50px}
.nav::before,.nav::after{content:"";position:absolute;top:0;border:3px solid transparent;border-bottom-color:#222}
.nav::before{left:-6px;border-right-color:#222}
.nav::after{right:-6px;border-left-color:#222}
.nav-item{display:flex;align-items:center;gap:8px}
.nav-icon{width:50px;height:50px;border-radius:50%;background:#0d6e9e;display:flex;align-items:center;justify-content:center}
.nav-icon span{width:40px;height:40px;border-radius:50%;background:#fff;display:flex;align-items:center;justify-content:center}
.nav-text{color:#fff;font-size:15.5px;margin-top:-4px}
.nav-text b{font-weight:400;display:block}
.nav-text i{font-style:normal;display:inline-block;margin-top:4px;background:#fff;color:#777;font-size:12px;padding:3px 10px;border-radius:2px}
.titlebar{top:121px;height:49px;border-bottom:1px solid var(--line);display:flex;justify-content:space-between;align-items:center}
.titlebar h1{font-size:22px;font-weight:400;color:#666}
.crumb{font-size:12.5px;color:#c5c5c5}
.crumb a{color:var(--blue);text-decoration:none;margin-right:4px}
.panel{position:absolute;background:var(--panel);border:1px solid #e8e8e8}
.panel-head{background:var(--blue);color:#fff;display:flex;align-items:center;gap:10px;padding-left:12px;font-size:16.5px;margin:-1px -1px 0}
.welcome{left:161px;top:188px;width:878px;height:209px}
.welcome .panel-head{height:34px;font-weight:500;font-size:15.5px}
.notice{margin:14px 23px 0;height:29px;background:#e6e6e6;display:flex;justify-content:space-between;align-items:center;padding-left:11px;font-size:16px;color:#444}
.notice span.ok{background:var(--grey-btn);color:#fff;height:100%;padding:0 16px;display:flex;align-items:center;font-weight:500;font-size:14.5px}
.welcome p{margin:12px 23px 0;font-size:11.9px;line-height:20.6px;color:#555}
.chart{top:419px;height:291px}
.chart .panel-head,.stat .panel-head{height:38px}
.left{left:161px;width:427px}
.right{left:610px;width:429px}
.stat{top:734px;height:290px}
.stat-body{padding:16px 18px 0}
.toolbar{background:#fff;height:40px;display:flex;justify-content:space-between;align-items:center;padding:0 8px}
.select{width:49px;height:27px;border:1px solid #ddd;font-size:12.5px;display:flex;align-items:center;justify-content:space-between;padding:0 7px;color:#444}
.search{display:flex;height:27px;border:1px solid #ddd}
.search span{width:31px;border-right:1px solid #ddd;background:#f4f4f4;display:flex;align-items:center;justify-content:center}
.search em{font-style:normal;width:139px;font-size:12.5px;color:#aaa;padding-left:7px;display:flex;align-items:center;background:#fff}
table{border-collapse:collapse;width:100%;table-layout:fixed}
th{height:33px;text-align:left;font-size:14px;font-weight:500;color:#444;padding-left:8px;border:1px solid #ddd;background:#f4f4f4;position:relative}
th::after{content:"⬍";position:absolute;right:6px;top:11px;font-size:8px;color:#bbb}
th.sorted::after{content:"▲";color:#444;font-size:7px;top:13px}
td{height:26.5px;font-size:12px;color:var(--muted);padding-left:9px;border:1px solid #ddd;background:#fff}
.bar{width:55px;height:6px;border:1px solid #ccc;background:#fff}
.bar i{display:block;height:100%;background:var(--blue)}
.foot{display:flex;justify-content:space-between;align-items:center;margin-top:15px}
.foot b{font-size:14px;font-weight:500;color:#444}
.pager{display:flex;border:1px solid #ddd;background:#fff}
.pager span{width:29px;height:27px;display:flex;align-items:center;justify-content:center;font-size:14px;color:#666;border-left:1px solid #ddd}
.pager span:first-child{border-left:0;color:#bbb}
.pager span.on{background:var(--blue);color:#fff}
.pager span:last-child{color:#bbb}
.footer{position:absolute;top:1046px;left:0;width:1200px;height:58px;background:var(--footer);color:#fff;font-size:13.5px;display:flex;align-items:center;justify-content:center}
.footer a{color:var(--blue);text-decoration:none}
</style>
</head>
<body>
<div class="topline"></div>
<div class="stripe"></div>

<div class="wrap logo">LOGO HERE</div>
<div class="userbar">
  <div class="ibtn"><svg width="16" height="12" viewBox="0 0 16 12"><rect x=".5" y=".5" width="15" height="11" fill="none" stroke="#fff"/><path d="M.5 .5 8 7l7.5-6.5" fill="none" stroke="#fff"/></svg></div>
  <div class="ibtn"><svg width="16" height="16" viewBox="0 0 16 16"><circle cx="8" cy="8" r="5" fill="none" stroke="#fff" stroke-width="3" stroke-dasharray="2.2 1.7"/><circle cx="8" cy="8" r="3.5" fill="#fff"/><circle cx="8" cy="8" r="1.5" fill="var(--icon-btn)"/></svg></div>
  <div class="ibtn"><svg width="14" height="15" viewBox="0 0 14 15"><circle cx="7" cy="4.5" r="3.8" fill="#fff"/><path d="M0 15c0-5 3-6.5 7-6.5s7 1.5 7 6.5z" fill="#fff"/></svg></div>
  <div class="user">Jonas Weber<span class="caret"><svg width="10" height="6" viewBox="0 0 10 6"><path d="M1 1l4 4 4-4" fill="none" stroke="#fff" stroke-width="1.4"/></svg></span></div>
</div>

<nav class="wrap nav">
  <div class="nav-item"><div class="nav-icon"><span><svg width="22" height="20" viewBox="0 0 22 20"><rect x="1" y="1" width="20" height="13" rx="1" fill="#0d6e9e"/><rect x="3" y="3" width="16" height="9" fill="#fff"/><rect x="9" y="14" width="4" height="3" fill="#0d6e9e"/><rect x="6" y="17" width="10" height="2" fill="#0d6e9e"/></svg></span></div><div class="nav-text"><b>DASHBOARD</b><i>Click Here</i></div></div>
  <div class="nav-item"><div class="nav-icon"><span><svg width="20" height="20" viewBox="0 0 20 20"><circle cx="10" cy="6" r="5" fill="#0d6e9e"/><path d="M1 20c0-6 4-8 9-8s9 2 9 8z" fill="#0d6e9e"/></svg></span></div><div class="nav-text"><b>MY PROFILE</b><i>Click Here</i></div></div>
  <div class="nav-item"><div class="nav-icon"><span><svg width="22" height="20" viewBox="0 0 22 20"><path d="M3 14V11a8 8 0 0 1 16 0v3" fill="none" stroke="#0d6e9e" stroke-width="2.5"/><rect x="2" y="12" width="5" height="7" rx="1.5" fill="#0d6e9e"/><rect x="15" y="12" width="5" height="7" rx="1.5" fill="#0d6e9e"/></svg></span></div><div class="nav-text"><b>AUDIO ADMIN</b><i>Click Here</i></div></div>
</nav>

<div class="wrap titlebar"><h1>DASHBOARD</h1><div class="crumb"><a href="#">Home</a>› Dashboard</div></div>

<section class="panel welcome">
  <div class="panel-head"><svg width="20" height="17" viewBox="0 0 20 17"><rect x="1" y="1" width="18" height="15" fill="none" stroke="#fff" stroke-width="1.5"/><circle cx="6" cy="6" r="1.8" fill="#fff"/><path d="M2 15l5-5 3 3 4-5 5 7z" fill="#fff"/></svg>Willkommen : Name Here</div>
  <div class="notice">Vestibulum ante ipsum primis in faucibus orci luctus et ultrices posuere<span class="ok">Alles OK</span></div>
  <p>Lorem ipsum dolor sit amet, consectetur adipiscing elit. Donec congue auctor est, id convallis purus eleifend dictum. Nulla ornare, quam at tristique iaculis, metus massa venenatis odio, at rutrum ipsum eros vel sem. Integer faucibus nibh vehicula ultrices luctus. Vestibulum at tortor purus. Curabitur placerat leo nec luctus semper. Etiam quis nisl ut ante scelerisque faucibus et vel magna. Nunc venenatis vehicula tempus. Vestibulum massa felis, convallis ac consequat non, sodales lobortis turpis. Proin nec pretium magna, faucibus malesuada urna.</p>
</section>

<section class="panel chart left">
  <div class="panel-head"><svg width="22" height="20" viewBox="0 0 22 20"><rect x="1" y="1" width="20" height="18" fill="none" stroke="#fff" stroke-width="1.6"/><rect x="5" y="6" width="2.5" height="10" fill="#fff"/><rect x="9.5" y="9" width="2.5" height="7" fill="#fff"/><rect x="14" y="11" width="2.5" height="5" fill="#fff"/></svg>Velto Trend Fur</div>
  <svg width="427" height="252" viewBox="0 0 498 294" font-family="Roboto,sans-serif" font-size="18" fill="#555">
    <g stroke="#e4e4e4" stroke-width="1">
      <line x1="40" y1="27" x2="470" y2="27"/><line x1="40" y1="73" x2="470" y2="73"/><line x1="40" y1="119" x2="470" y2="119"/><line x1="40" y1="166" x2="470" y2="166"/><line x1="40" y1="212" x2="470" y2="212"/><line x1="40" y1="259" x2="470" y2="259"/>
      <line x1="40" y1="27" x2="40" y2="259"/><line x1="470" y1="27" x2="470" y2="259"/>
    </g>
    <g text-anchor="end"><text x="33" y="33">25</text><text x="33" y="79">20</text><text x="33" y="125">15</text><text x="33" y="172">10</text><text x="33" y="218">5</text><text x="33" y="264">0</text></g>
    <g text-anchor="middle"><text x="52" y="277">Dec</text><text x="119" y="277">Jan</text><text x="187" y="277">Feb</text><text x="254" y="277">Mar</text><text x="322" y="277">Apr</text><text x="396" y="277">May</text><text x="467" y="277">June</text></g>
    <polyline points="40,226 114,178 170,112 233,99 268,140 327,87 368,102 413,70 470,151" fill="none" stroke="var(--s1)" stroke-width="2.2"/>
    <g fill="var(--s1)"><circle cx="40" cy="226" r="4"/><circle cx="114" cy="178" r="4"/><circle cx="170" cy="112" r="4"/><circle cx="233" cy="99" r="4"/><circle cx="268" cy="140" r="4"/><circle cx="327" cy="87" r="4"/><circle cx="368" cy="102" r="4"/><circle cx="413" cy="70" r="4"/><circle cx="470" cy="151" r="4"/></g>
  </svg>
</section>

<section class="panel chart right">
  <div class="panel-head"><svg width="22" height="22" viewBox="0 0 22 22"><circle cx="11" cy="11" r="10" fill="#fff"/><path d="M11 11V1.5A9.5 9.5 0 0 1 20.5 11z" fill="var(--blue)"/></svg>Pie Chart</div>
  <svg width="429" height="252" viewBox="0 0 500 294" font-family="Roboto,sans-serif" font-size="17" fill="#555">
    <path d="M229 144V23A121 121 0 0 1 248 263.5z" fill="var(--s1)" stroke="#fff" stroke-width="2"/>
    <path d="M229 144L248 263.5A121 121 0 0 1 142 228z" fill="var(--s3)" stroke="#fff" stroke-width="2"/>
    <path d="M229 144L142 228A121 121 0 0 1 229 23z" fill="var(--s2)" stroke="#fff" stroke-width="2"/>
    <rect x="401" y="14" width="20" height="13" fill="var(--s1)" stroke="#ddd"/><text x="429" y="26">Series1</text>
    <rect x="401" y="35" width="20" height="13" fill="var(--s2)" stroke="#ddd"/><text x="429" y="47">Series2</text>
    <rect x="401" y="57" width="20" height="13" fill="var(--s3)" stroke="#ddd"/><text x="429" y="69">Series3</text>
  </svg>
</section>

<section class="panel stat left">
  <div class="panel-head"><svg width="22" height="20" viewBox="0 0 22 20"><rect x="1" y="1" width="20" height="18" fill="none" stroke="#fff" stroke-width="1.6"/><rect x="5" y="6" width="2.5" height="10" fill="#fff"/><rect x="9.5" y="9" width="2.5" height="7" fill="#fff"/><rect x="14" y="11" width="2.5" height="5" fill="#fff"/></svg>Stat1</div>
  <div class="stat-body">
    <div class="toolbar"><div class="select">5<svg width="9" height="6" viewBox="0 0 9 6"><path d="M1 1l3.5 3.5L8 1" fill="none" stroke="#555" stroke-width="1.4"/></svg></div><div class="search"><span><svg width="14" height="14" viewBox="0 0 14 14"><circle cx="5" cy="5" r="3.8" fill="none" stroke="#555" stroke-width="1.8"/><path d="M8 8l5 5" stroke="#555" stroke-width="2.2"/></svg></span><em>Search</em></div></div>
    <table>
      <colgroup><col style="width:75px"><col style="width:101px"><col style="width:128px"><col style="width:86px"></colgroup>
      <tr><th>Name</th><th class="sorted">Position</th><th>Start Date</th><th>Salary</th></tr>
      <tr><td>John</td><td>Chefin</td><td>15-06-2014</td><td>Salami</td></tr>
      <tr><td>John</td><td>Chefin</td><td>15-06-2014</td><td>Salami</td></tr>
      <tr><td>John</td><td>Chefin</td><td>15-06-2014</td><td>Salami</td></tr>
      <tr><td>John</td><td>Chefin</td><td>15-06-2014</td><td>Salami</td></tr>
    </table>
    <div class="foot"><b>1-5 of 10</b><div class="pager"><span>‹</span><span class="on">1</span><span>2</span><span>›</span></div></div>
  </div>
</section>

<section class="panel stat right">
  <div class="panel-head"><svg width="22" height="20" viewBox="0 0 22 20"><rect x="1" y="1" width="20" height="18" fill="none" stroke="#fff" stroke-width="1.6"/><rect x="5" y="6" width="2.5" height="10" fill="#fff"/><rect x="9.5" y="9" width="2.5" height="7" fill="#fff"/><rect x="14" y="11" width="2.5" height="5" fill="#fff"/></svg>Stat 2</div>
  <div class="stat-body">
    <div class="toolbar"><div class="select">5<svg width="9" height="6" viewBox="0 0 9 6"><path d="M1 1l3.5 3.5L8 1" fill="none" stroke="#555" stroke-width="1.4"/></svg></div><div class="search"><span><svg width="14" height="14" viewBox="0 0 14 14"><circle cx="5" cy="5" r="3.8" fill="none" stroke="#555" stroke-width="1.8"/><path d="M8 8l5 5" stroke="#555" stroke-width="2.2"/></svg></span><em>Search</em></div></div>
    <table>
      <colgroup><col style="width:106px"><col style="width:82px"><col style="width:131px"><col style="width:71px"></colgroup>
      <tr><th>Domain</th><th class="sorted">Niveau</th><th>Keyw</th><th>SE Key</th></tr>
      <tr><td>praxis1.de</td><td><div class="bar"><i style="width:10%"></i></div></td><td>Gemeinsame Key</td><td>SE Key</td></tr>
      <tr><td>praxis1.de</td><td><div class="bar"><i style="width:20%"></i></div></td><td>Gemeinsame Key</td><td>SE Key</td></tr>
      <tr><td>praxis1.de</td><td><div class="bar"><i style="width:30%"></i></div></td><td>Gemeinsame Key</td><td>SE Key</td></tr>
      <tr><td>praxis1.de</td><td><div class="bar"><i style="width:45%"></i></div></td><td>Gemeinsame Key</td><td>SE Key</td></tr>
    </table>
    <div class="foot"><b>1-5 of 10</b><div class="pager"><span>‹</span><span class="on">1</span><span>2</span><span>›</span></div></div>
  </div>
</section>

<footer class="footer">2014 ©&nbsp;<a href="#">domain name</a>. All rights reserved</footer>
</body>
</html>
```